Harrowgate Distillery Bottle Label Design

We need a label design for a product called "Cedar Lorne Straight Bourbon Whiskey". The bottle has two embossments on the side and an image printed on the back that will show through when looking from the front (shown in the attached image). It's made of 30% rye and 70% corn; images of the ingredients can be incorporated into the label design. We are a distillery that produces whiskey and bourbon from local farmers around the area. We focus on the quality of the ingredients and using the recipes passed down from generation to generation. We like a straight forward design using two colors maximum. The background will be brown once filled with the bourbon, so it must contrast against it (i.e. white and other lighter colors). The Harrowgate Distillery logo must be present on the bottle front, as well as 750 ml, 84 PROOF, 42% ALC/VOL.

Target Market(s)

Craft whiskey consumers.

Industry/Entity Type

Product

Colors
fee18a
fbe7d2
fff3d1
fefcee
fefdec
fdf9cf

Requirements
Must have
• 750 ml, 84 PROOF, 42% ALC/VOL. Aged for 3 years.The Harrowgate Distillery logo must be present on the bottle. Only two colors on label.
Nice to have
• Story of how we are a micro distillery making hand crafted whiskey.
Should not have
• False or misleading print.

```html
<!DOCTYPE html>
<html lang="en">
<head>
<meta charset="utf-8">
<title>Cedar Lorne Straight Bourbon Whiskey – Label</title>
<link rel="stylesheet" href="https://fonts.googleapis.com/css2?family=Montserrat:wght@300;700;800&family=Rye&display=swap">
<style>
  :root {
    --backdrop-centre: #fbfbfb;
    --backdrop-edge: #d9dadb;
    --bottle-fill: #ffffff;
    --dieline: #2aa7df;
    --gold: #a98b2d;
    --sand: #d8c9b6;
    --sand-dark: #c9b8a2;
  }
  * { margin: 0; padding: 0; box-sizing: border-box; }
  html, body { width: 737px; height: 1200px; overflow: hidden; }
  body {
    position: relative;
    background: radial-gradient(ellipse at 50% 45%, var(--backdrop-centre) 0%, var(--backdrop-centre) 30%, var(--backdrop-edge) 100%);
    font-family: "Montserrat", Arial, sans-serif;
  }
  .bottle { position: absolute; left: 0; top: 0; }
  .label { position: absolute; left: 0; top: 0; width: 737px; height: 1200px; }

  .maker {
    position: absolute; left: 0; width: 737px; top: 418px;
    display: flex; flex-direction: column; align-items: center; gap: 8px;
  }
  .maker-dot { width: 30px; height: 30px; border-radius: 50%; background: var(--gold); }
  .maker-name {
    color: var(--gold); font-weight: 700; font-size: 12px; letter-spacing: 2.5px;
    text-align: center; line-height: 1.45; text-transform: uppercase;
  }

  .still-art {
    position: absolute; left: 260px; top: 534px; width: 208px; height: 218px;
    background: linear-gradient(180deg, #e6dbcd 0%, var(--sand) 100%);
    border-radius: 4px;
  }

  .product-name {
    position: absolute; left: 0; width: 737px; top: 754px; text-align: center;
    font-family: "Rye", Georgia, serif; font-size: 35px; color: var(--gold);
    letter-spacing: 0.5px; line-height: 1;
  }
  .name-rule {
    position: absolute; left: 350px; top: 800px; width: 38px; height: 1px; background: var(--sand);
  }
  .product-type {
    position: absolute; left: 0; width: 737px; top: 815px; text-align: center;
    font-weight: 700; font-size: 10.5px; color: var(--sand-dark); letter-spacing: 0.4px;
    text-transform: uppercase;
  }

  .age-caption {
    position: absolute; left: 0; width: 737px; text-align: center;
    font-weight: 700; color: var(--sand-dark); text-transform: uppercase;
  }
  .age-caption.top { top: 867px; font-size: 5.5px; letter-spacing: 2px; }
  .age-caption.bottom { top: 918px; font-size: 7px; letter-spacing: 1px; }
  .age-number {
    position: absolute; left: 0; width: 737px; top: 874px; text-align: center;
    font-weight: 800; font-size: 40px; line-height: 1; color: var(--gold);
  }
  .age-lines { position: absolute; left: 0; top: 0; }

  .proof {
    position: absolute; left: 299px; top: 931px; width: 127px; text-align: center;
    font-weight: 700; font-size: 15px; color: var(--sand-dark); line-height: 30px;
  }
  .volume, .strength {
    position: absolute; top: 968px; font-weight: 300; font-size: 11.5px;
    color: var(--sand-dark); letter-spacing: 0.3px;
  }
  .volume { left: 262px; }
  .volume small { font-size: 8.5px; }
  .strength { left: 350px; }
</style>
</head>
<body>
  <svg class="bottle" width="737" height="1200" viewBox="0 0 737 1200" aria-hidden="true">
    <path d="M304,192 L304,298 C304,318 296,326 280,336 C240,362 214,390 212,450 L212,1030 C212,1080 226,1108 250,1108 L472,1108 C496,1108 510,1080 510,1030 L510,450 C508,390 482,362 442,336 C426,326 419,318 419,298 L419,192 Z"
          fill="var(--bottle-fill)" stroke="var(--dieline)" stroke-width="0.8"/>
    <rect x="299" y="150" width="124" height="42" rx="2" fill="var(--bottle-fill)" stroke="var(--dieline)" stroke-width="0.8"/>
    <path d="M242,1106 C300,1090 330,1084 361,1084 C392,1084 422,1090 480,1106"
          fill="none" stroke="var(--dieline)" stroke-width="0.8" stroke-dasharray="4 3"/>
  </svg>

  <div class="label">
    <div class="maker">
      <span class="maker-dot"></span>
      <p class="maker-name">Harrowgate<br>Distillery</p>
    </div>

    <div class="still-art" role="img" aria-label="Engraved illustration of a copper pot still joined by a pipe to a condenser on a brick base"></div>

    <h1 class="product-name">Cedar Lorne</h1>
    <div class="name-rule"></div>
    <p class="product-type">Straight Bourbon Whiskey</p>

    <p class="age-caption top">Aged for</p>
    <svg class="age-lines" width="737" height="1200" viewBox="0 0 737 1200" aria-hidden="true">
      <g stroke="var(--sand)" stroke-width="1">
        <line x1="320" y1="882" x2="340" y2="882"/>
        <line x1="310" y1="890" x2="340" y2="890"/>
        <line x1="310" y1="900" x2="340" y2="900"/>
        <line x1="320" y1="908" x2="340" y2="908"/>
        <line x1="388" y1="882" x2="408" y2="882"/>
        <line x1="388" y1="890" x2="418" y2="890"/>
        <line x1="388" y1="900" x2="418" y2="900"/>
        <line x1="388" y1="908" x2="408" y2="908"/>
        <line x1="288" y1="930" x2="436" y2="930"/>
        <line x1="299" y1="930" x2="299" y2="962"/>
        <line x1="426" y1="930" x2="426" y2="962"/>
        <line x1="234" y1="962" x2="491" y2="962"/>
        <line x1="330" y1="966" x2="330" y2="986"/>
        <line x1="234" y1="989" x2="491" y2="989"/>
      </g>
    </svg>
    <p class="age-number">3</p>
    <p class="age-caption bottom">Years</p>

    <p class="proof">84 PROOF</p>
    <p class="volume">750 <small>ML</small></p>
    <p class="strength">42% ALC/VOL.</p>
  </div>
</body>
</html>
```